Website for Plumbing Company, Palmetto Hot Water

I need a 7-page fully HTML-coded website for my plumbing company, Palmetto Hot Water. We specialize in installation, repair, and replacement of both gas and electric water heaters. Although we offer both tankless (on-demand) water heaters and standard (with tank) water heaters, most of our business is related to standard (with tank) water heaters in the USA market.

These are the pages I need:
1. Home page with sections such as About Us, Our Services, Why Choose Us, Testimonials, Location Map (Palm Beach County Florida), Quote Request Form, Join Our Newsletter, Mission Statement, etc.

2. Gas Water Heaters

3. Electric Water Heaters

4. Tankless Water Heaters

5. About Us

6. Contact Us

7. Privacy Policy, Terms & Conditions

Be sure to mention the following points:
1. Same-Day Service
2. Best Price Guarantee
3. 100% Satisfaction Rating
4. 15-Year Warranty on Water Heater & Parts
5. Lifetime Warranty on Workmanship
*All Warranties are Transferrable Upon Home Sale

Once design is selected and finalized, I need the website coded in a standard HTML/CSS and temporarily hosted on your development server so I can see the website functionality that is not observable from screenshots, such as section animations, etc. Once those details are finalized, I will move the source code to my server and complete the project.

Target Market(s)

Residential Home Owners and Business Owners

Industry/Entity Type

Plumbing, Home Services, Remodeling, Construction

Coding

Coded - Design and coding required

Number of Pages Required

5+ page

Colors
0054AA
0677BA
7BADD7
CADEEF
E8F1F8
FFC000
F8CF3A
FAE287
FDF2CF
FEFAEE
EE7325
F08F49
F5BC92
FAE3D3
FDF4ED

Requirements
Must have
• Clean, colorful, and professional

```html
<!DOCTYPE html>
<html lang="en">
<head>
<meta charset="UTF-8">
<title>Palmetto Hot Water – Water Heater Services</title>
<link href="https://fonts.googleapis.com/css2?family=Barlow:wght@400;500;600;700&family=Barlow+Semi+Condensed:wght@500;600;700&display=swap" rel="stylesheet">
<style>
:root{
  --navy:#1d4689;
  --navy-dark:#163a74;
  --blue:#2c5ea8;
  --sky:#7badd7;
  --ice:#e8f1f8;
  --orange:#e8621f;
  --orange-light:#f08f49;
  --ink:#1f2c44;
  --muted:#5a6478;
  --line:#c9d3e2;
  --stage:#e4e7ed;
  --white:#ffffff;
  --soft:#f4f6fa;
}
*{box-sizing:border-box;margin:0;padding:0}
html,body{width:800px;height:1200px;overflow:hidden}
body{background:var(--stage);font-family:'Barlow',sans-serif;color:var(--ink);position:relative}
.page{position:absolute;left:146px;top:0;width:508px;height:1180px;background:var(--soft);overflow:hidden}
.abs{position:absolute}
.head{font-family:'Barlow Semi Condensed',sans-serif;font-weight:700}
.btn{display:flex;align-items:center;justify-content:center;color:#fff;font-weight:600;font-size:9px;border-radius:2px}
.btn-orange{background:var(--orange)}
.btn-navy{background:var(--navy)}

.site-header{left:0;top:0;width:508px;height:36px;background:var(--navy)}
.brand{position:absolute;left:30px;top:10px;display:flex;align-items:center;gap:5px;color:#fff;font-size:13px;font-weight:700;white-space:nowrap}
.brand-dot{width:12px;height:12px;border-radius:50%;background:var(--orange)}
.header-phone{position:absolute;left:290px;top:11px;color:#fff;font-size:10px;display:flex;align-items:center;gap:4px;white-space:nowrap}
.header-cta{left:381px;top:7px;width:80px;height:20px;font-size:7.5px}

.hero{left:0;top:36px;width:508px;height:150px;background:linear-gradient(90deg,#c9d9ef 0%,#b7cde9 45%,#8eaedb 100%)}
.hero-photo{left:260px;top:0;width:248px;height:150px;background:linear-gradient(135deg,#9db8df,#d4dde8 55%,#aebcd0)}
.hero-title{left:40px;top:20px;width:260px;text-align:center;font-size:20px;line-height:25px;color:var(--navy)}
.hero-title span{font-weight:600;color:var(--blue)}
.hero-tags{left:94px;top:77px;width:168px;text-align:center;font-size:8.5px;font-weight:600;color:var(--navy-dark);border-top:1px solid var(--sky);border-bottom:1px solid var(--sky);padding:3px 0}
.hero-quote{left:64px;top:102px;width:107px;height:23px;font-size:9px}
.hero-call{left:185px;top:102px;width:66px;height:23px;font-size:9px}

.about-band{left:0;top:186px;width:508px;height:30px;background:var(--navy)}
.about-card{left:24px;top:188px;width:459px;height:100px;background:#fff;box-shadow:0 2px 6px rgba(0,0,0,.15)}
.about-title{left:22px;top:14px;font-size:13px;color:var(--navy)}
.about-rule{left:80px;top:23px;width:220px;height:1px;background:var(--line)}
.about-lead{left:22px;top:42px;font-size:7.5px;font-weight:600}
.about-text{left:22px;top:55px;width:270px;font-size:7px;line-height:11px;color:var(--ink)}
.about-text b{font-weight:500;color:var(--navy)}
.about-bar{left:22px;top:83px;width:45px;height:3px;background:var(--sky)}
.about-photo{left:312px;top:13px;width:126px;height:80px;border-radius:4px;background:linear-gradient(135deg,#b9c4d2,#7d93b5 60%,#2f5590)}

.sec-title{width:508px;text-align:center;font-size:16px;color:var(--navy);white-space:nowrap}
.sec-title::before,.sec-title::after{content:"";display:inline-block;width:130px;height:1px;background:var(--line);vertical-align:middle;margin:0 10px}

.services{left:0;top:290px;width:508px;height:136px;background:#fff}
.card-row{position:absolute;left:38px;width:432px;display:flex}
.card{flex:1;text-align:center;position:relative}
.card + .card{border-left:1px solid #e1e6ee}
.card-icon{width:42px;height:42px;margin:0 auto;border-radius:6px}
.card-name{font-size:8px;font-weight:700;color:var(--navy-dark);margin-top:14px;white-space:nowrap}
.card-desc{font-size:6px;line-height:8px;color:var(--muted);margin-top:5px;padding:0 10px}

.why{left:0;top:426px;width:508px;height:127px;background:#f6f8fb}
.why .card-name{margin-top:8px}
.why-icon{height:32px;display:flex;align-items:center;justify-content:center}

.mission{left:0;top:553px;width:508px;height:97px;background:linear-gradient(180deg,#2e5aa0,#264d8f 60%,#4d6f9f)}
.mission-title{top:14px;color:#fff}
.mission-title::before,.mission-title::after{background:rgba(255,255,255,.5);width:150px}
.mission-sub{top:44px;width:508px;text-align:center;color:#fff;font-size:10px;font-weight:500}
.mission-text{top:64px;width:508px;text-align:center;color:#fff;font-size:8px;line-height:13px}
.dots{display:flex;gap:4px}
.dots i{width:4px;height:4px;border-radius:50%;background:#c5cedd;display:block}
.dots i.on{background:var(--navy)}
.dots i.hot{background:var(--orange)}

.testi-title{top:667px}
.testi-card{left:36px;top:691px;width:436px;height:57px;background:#fff;box-shadow:0 1px 4px rgba(0,0,0,.12);border-radius:3px}
.avatar{left:12px;top:7px;width:38px;height:38px;border-radius:50%;background:linear-gradient(135deg,#6d86ad,#2b4d86);border:2px solid #dbe3ee}
.quote-mark{left:60px;top:8px;font-size:20px;color:#aab8cf;font-weight:700;line-height:20px}
.quote-text{left:78px;top:13px;font-size:7.5px;color:var(--ink);white-space:nowrap}
.quote-text b{color:var(--navy)}
.quote-name{left:80px;top:25px;font-size:7px}
.arrow-btn{width:14px;height:22px;background:#fff;border:1px solid #d5dbe6;display:flex;align-items:center;justify-content:center}

.area{left:0;top:762px;width:508px;height:179px;background:linear-gradient(180deg,#3d69ad 0%,#5a80b6 45%,#6b8a9d 75%,#3a6099 100%)}
.area-title{left:44px;top:16px;font-size:15px;color:#fff}
.area-title::after{content:"";display:inline-block;width:32px;height:1px;background:rgba(255,255,255,.7);vertical-align:middle;margin-left:8px}
.area-sub{left:44px;top:45px;font-size:8px;color:#fff;font-weight:500}
.area-map{left:208px;top:15px;width:264px;height:152px;border-radius:2px;background:linear-gradient(110deg,#d8e3c4 0%,#cfe0b8 35%,#9fc3ec 50%,#d8e3c4 62%,#cfe3b9 85%,#8eb8e6 100%)}

.quote-title{top:954px}
.field{background:#fff;border:1px solid #e0e5ee;font-size:7.5px;color:var(--ink);display:flex;align-items:center;padding-left:10px;font-weight:500}
.field.placeholder{color:#a4acba}
.chev{position:absolute;right:8px;top:50%;transform:translateY(-50%)}
.quote-btn{left:184px;top:1081px;width:133px;height:26px;font-size:12px;font-weight:700;font-family:'Barlow Semi Condensed',sans-serif;border-radius:2px}

.newsletter{left:0;top:1116px;width:508px;height:39px;background:var(--navy)}
.news-title{left:66px;top:11px;color:#fff;font-size:12px}
.news-sub{left:182px;top:14px;color:#fff;font-size:7px}
.news-input{left:286px;top:9px;width:94px;height:19px;background:#fff;font-size:7px;color:#8c94a3;display:flex;align-items:center;padding-left:8px}
.news-btn{left:384px;top:9px;width:60px;height:19px;font-size:7.5px}
.footer{left:0;top:1155px;width:508px;height:25px;background:var(--navy-dark);color:#fff;font-size:6.5px}
.footer-left{left:38px;top:8px}
.footer-nav{left:225px;top:8px;display:flex;gap:5px}
.social{width:10px;height:10px;border-radius:50%;top:7px}
</style>
</head>
<body>
<main class="page">

  <header class="abs site-header">
    <div class="brand"><span class="brand-dot"></span>Palmetto Hot Water</div>
    <div class="header-phone">
      <svg width="9" height="9" viewBox="0 0 24 24"><path fill="#fff" d="M6.6 10.8a15 15 0 0 0 6.6 6.6l2.2-2.2a1 1 0 0 1 1-.25 11.4 11.4 0 0 0 3.6.57 1 1 0 0 1 1 1V20a1 1 0 0 1-1 1A17 17 0 0 1 3 4a1 1 0 0 1 1-1h3.5a1 1 0 0 1 1 1c0 1.25.2 2.45.57 3.57a1 1 0 0 1-.25 1z"/></svg>
      (561) 555-0148
    </div>
    <div class="abs btn btn-orange header-cta">Request a Quote</div>
  </header>

  <section class="abs hero">
    <div class="abs hero-photo" role="img" aria-label="Smiling technician in blue uniform beside a tank water heater"></div>
    <h1 class="abs head hero-title">Professional Water Heater<br>Services in <span>Palm Beach County</span></h1>
    <div class="abs hero-tags">Gas &middot; Electric &middot; Tank &amp; Tankless</div>
    <div class="abs btn btn-orange hero-quote">Request a Quote</div>
    <div class="abs btn btn-navy hero-call">Call Now</div>
  </section>

  <div class="abs about-band"></div>
  <section class="abs about-card">
    <h2 class="abs head about-title">About Us</h2>
    <div class="abs about-rule"></div>
    <p class="abs about-lead">Your Local Water Heater Experts.</p>
    <p class="abs about-text">Specializing in installation, repair and replacement of water heaters throughout Palm Beach County. Licensed &amp; Insured. &nbsp;<b>Learn More &rsaquo;</b></p>
    <div class="abs about-bar"></div>
    <div class="abs about-photo" role="img" aria-label="Technician working on a water heater installation"></div>
  </section>

  <section class="abs services">
    <h2 class="abs head sec-title" style="top:11px">Our Services</h2>
    <div class="card-row" style="top:42px">
      <div class="card"><div class="card-icon" role="img" aria-label="Gas water heater illustration" style="background:linear-gradient(135deg,#5a86c4,#1d4689)"></div><div class="card-name">Gas Water Heaters</div><div class="card-desc">Clean burning gas units &amp; instant recovery heaters.</div></div>
      <div class="card"><div class="card-icon" role="img" aria-label="Electric water heater illustration" style="background:linear-gradient(135deg,#3f70b8,#c9d5e6)"></div><div class="card-name">Electric Water Heaters</div><div class="card-desc">Efficient electric models for every size home.</div></div>
      <div class="card"><div class="card-icon" role="img" aria-label="Tank and tankless heater illustration" style="background:linear-gradient(135deg,#9fb6d6,#40679f)"></div><div class="card-name">Tank &amp; Tankles Heaters</div><div class="card-desc">Tank and tankless options for quality hot water.</div></div>
      <div class="card"><div class="card-icon" role="img" aria-label="Emergency alarm light illustration" style="background:linear-gradient(180deg,#f08f49,#d8401f)"></div><div class="card-name">Emergency Replacement</div><div class="card-desc">Fast repair and replacement when your heater fails.</div></div>
    </div>
  </section>

  <section class="abs why">
    <h2 class="abs head sec-title" style="top:18px">Why Choose Us</h2>
    <div class="card-row" style="top:51px">
      <div class="card"><div class="why-icon"><svg width="26" height="26" viewBox="0 0 26 26"><path d="M13 1l10 5v7c0 6-4.5 10-10 12C7.5 23 3 19 3 13V6z" fill="#1d4689"/><path d="M8 13l3.5 3.5L18 10" stroke="#fff" stroke-width="2.4" fill="none"/></svg></div><div class="card-name">Licensed &amp; Insured</div><div class="card-desc">Fully licensed for every water replacement.</div></div>
      <div class="card"><div class="why-icon"><svg width="30" height="28" viewBox="0 0 30 28"><circle cx="15" cy="14" r="11" fill="none" stroke="#1d4689" stroke-width="2.2"/><path d="M3 18c2 5 5 7 8 8M27 18c-2 5-5 7-8 8" stroke="#e8621f" stroke-width="2" fill="none"/><path d="M10 14l3.5 3.5L20 10" stroke="#1d4689" stroke-width="2.4" fill="none"/></svg></div><div class="card-name">Same-Day Service</div><div class="card-desc">Same-day repair for any broken heater.</div></div>
      <div class="card"><div class="why-icon"><svg width="32" height="24" viewBox="0 0 32 24"><rect x="1" y="2" width="30" height="20" rx="2" fill="#1d4689"/><rect x="1" y="6" width="30" height="3" fill="#7badd7"/><circle cx="10" cy="15" r="3" fill="#e8621f"/><rect x="16" y="13" width="11" height="2" fill="#fff"/><rect x="16" y="17" width="8" height="2" fill="#fff"/></svg></div><div class="card-name">Transparent Pricing</div><div class="card-desc">Clear quotes with no hidden heating fees.</div></div>
      <div class="card"><div class="why-icon"><div role="img" aria-label="Technician figure icon" style="width:26px;height:30px;border-radius:13px 13px 4px 4px;background:linear-gradient(180deg,#1d4689,#3f70b8)"></div></div><div class="card-name">Experienced Technicians</div><div class="card-desc">Trained pros for every water heater.</div></div>
    </div>
  </section>

  <section class="abs mission">
    <div class="abs" role="img" aria-label="Aerial view of a Palm Beach neighbourhood under a blue sky" style="left:0;top:0;width:508px;height:97px;background:linear-gradient(180deg,rgba(30,70,137,.2),rgba(120,150,170,.35))"></div>
    <h2 class="abs head sec-title mission-title">Our Mission</h2>
    <p class="abs mission-sub">Dedicated to Quality Service &amp; Customer Satisfaction</p>
    <p class="abs mission-text">Providing reliable and efficient water heater solutions with a<br>commitment to safety and excellence.</p>
  </section>
  <div class="abs dots" style="left:238px;top:653px"><i class="on"></i><i class="hot"></i><i></i><i></i></div>

  <h2 class="abs head sec-title testi-title" style="font-size:15px">Customer Testimonials</h2>
  <div class="abs arrow-btn" style="left:26px;top:709px"><svg width="6" height="10" viewBox="0 0 6 10"><path d="M5 1L1 5l4 4" stroke="#8893a6" fill="none"/></svg></div>
  <div class="abs arrow-btn" style="left:460px;top:709px"><svg width="6" height="10" viewBox="0 0 6 10"><path d="M1 1l4 4-4 4" stroke="#8893a6" fill="none"/></svg></div>
  <section class="abs testi-card">
    <div class="abs avatar" role="img" aria-label="Customer portrait"></div>
    <div class="abs quote-mark">&ldquo;</div>
    <p class="abs quote-text">Quick and reliable service! My water heater was replaced the same day. <b>Highly recommend!</b> &rdquo;</p>
    <p class="abs quote-name">- Dale R.</p>
  </section>
  <div class="abs dots" style="left:242px;top:745px"><i class="hot"></i><i class="on"></i><i></i></div>

  <section class="abs area">
    <div class="abs" role="img" aria-label="Aerial photo of waterfront homes in Palm Beach County" style="left:0;top:60px;width:208px;height:119px;background:linear-gradient(180deg,rgba(90,128,182,0),rgba(60,90,80,.45) 60%,rgba(58,96,153,.6))"></div>
    <h2 class="abs head area-title">Service Area</h2>
    <p class="abs area-sub">Proudly Serving Palm Beach County, FL</p>
    <div class="abs area-map" role="img" aria-label="Map of Palm Beach County with Lake Okeechobee and coastal towns"></div>
  </section>

  <h2 class="abs head sec-title quote-title" style="font-size:15px">Request a Quote</h2>
  <div class="abs field" style="left:43px;top:978px;width:139px;height:20px">Name</div>
  <div class="abs field" style="left:188px;top:978px;width:131px;height:20px">Phone</div>
  <div class="abs field" style="left:325px;top:978px;width:139px;height:20px">Email</div>
  <div class="abs field" style="left:43px;top:1006px;width:276px;height:21px">Service Needed<svg class="chev" width="7" height="5" viewBox="0 0 7 5"><path d="M1 1l2.5 2.5L6 1" stroke="#8893a6" fill="none"/></svg></div>
  <div class="abs field placeholder" style="left:325px;top:1006px;width:139px;height:21px">Message<svg class="chev" width="7" height="5" viewBox="0 0 7 5"><path d="M1 1l2.5 2.5L6 1" stroke="#8893a6" fill="none"/></svg></div>
  <div class="abs field" style="left:43px;top:1034px;width:421px;height:42px;align-items:flex-start;padding-top:8px">Message</div>
  <div class="abs btn btn-orange quote-btn">Get a Free Quote</div>

  <section class="abs newsletter">
    <h2 class="abs head news-title">Join Our Newsletter</h2>
    <p class="abs news-sub">Sign up for plumbing tips &amp;</p>
    <div class="abs news-input">Enter your email</div>
    <div class="abs btn btn-orange news-btn">Subscribe</div>
  </section>
  <footer class="abs footer">
    <div class="abs footer-left">Licensed &amp; Insured &nbsp;| &nbsp;Call Us: <b>(561) 555-0148</b></div>
    <nav class="abs footer-nav"><span>Home</span>&middot;<span>About Us</span>&middot;<span>Services</span>&middot;<span>Contact Us</span>&middot;<span>Privacy &amp; Terms</span></nav>
    <span class="abs social" style="left:441px;background:#fff"></span>
    <span class="abs social" style="left:457px;background:var(--orange)"></span>
  </footer>

</main>
</body>
</html>
```